Recycling Depot Business Card Design

We need a double sided business card for our recycling depot business. Please include name, position, address, phone, cell, fax, email and website address. Business card should match the colour scheme of our logo and look environmental but modern. I've attached a few business cards from Mintvale Works that I like.

Industry/Entity Type

Recycling

Contact Information for Business Card

Please include name, position, address, phone, cell, fax, email and website address.

Font styles to use
Sans Serif

Requirements
Must have
• Our Logo, Colour Scheme that matches our logo. Use of Colour Gradients and a custom look.

```html
<!DOCTYPE html>
<html lang="en">
<head>
<meta charset="utf-8">
<title>GreenLoop – Business Card</title>
<link rel="stylesheet" href="https://fonts.googleapis.com/css2?family=Poppins:wght@400;500;700&display=swap">
<style>
  :root {
    --page-bg: #2b2f33;
    --card-white: #ffffff;
    --green-dark: #1b6b34;
    --green-mid: #5ab946;
    --green-light: #9ccc3a;
    --text-dark: #1f3b27;
    --text-white: #ffffff;
  }
  * { margin: 0; padding: 0; box-sizing: border-box; }
  html, body { width: 1200px; height: 985px; overflow: hidden; }
  body {
    background: var(--page-bg);
    font-family: "Poppins", sans-serif;
    position: relative;
  }
  .card {
    position: absolute;
    left: 250px;
    width: 700px;
    height: 400px;
    border-radius: 22px;
    overflow: hidden;
    background: var(--card-white);
    box-shadow: 0 14px 30px rgba(0,0,0,.35);
  }
  .card--front { top: 70px; }
  .card--back { top: 515px; }
  .card__art { position: absolute; inset: 0; width: 100%; height: 100%; }

  .brand {
    position: absolute;
    display: flex;
    align-items: center;
    gap: 14px;
  }
  .brand__dot {
    width: 46px; height: 46px;
    border-radius: 50%;
    background: var(--green-mid);
  }
  .brand__name {
    font-weight: 700;
    font-size: 50px;
    line-height: 1;
    color: var(--green-dark);
  }
  .card--front .brand { left: 70px; top: 40px; }
  .card--back .brand { left: 50%; top: 152px; transform: translateX(-50%); }
  .card--back .brand__dot { width: 54px; height: 54px; }
  .card--back .brand__name { font-size: 58px; }

  .person {
    position: absolute;
    right: 48px;
    top: 122px;
    text-align: right;
  }
  .person__name {
    font-weight: 700;
    font-size: 22px;
    color: var(--green-dark);
    letter-spacing: .5px;
  }
  .person__role {
    font-size: 15px;
    color: var(--green-mid);
  }
  .contact {
    position: absolute;
    right: 48px;
    top: 196px;
    list-style: none;
  }
  .contact__item {
    display: flex;
    justify-content: flex-end;
    align-items: center;
    gap: 8px;
    font-size: 15px;
    line-height: 26px;
    color: var(--text-dark);
  }
  .contact__icon { width: 18px; height: 18px; flex: none; }

  .address {
    position: absolute;
    left: 46px;
    bottom: 30px;
    font-size: 16px;
    line-height: 1.35;
    color: var(--text-white);
  }
</style>
</head>
<body>

<section class="card card--front" aria-label="Business card front">
  <svg class="card__art" viewBox="0 0 700 400" aria-hidden="true">
    <defs>
      <linearGradient id="front-green" x1="0" y1="0" x2="1" y2="1">
        <stop offset="0" stop-color="#5ab946"/>
        <stop offset="1" stop-color="#9ccc3a"/>
      </linearGradient>
    </defs>
    <path d="M0,150 C200,160 340,270 500,400 L468,400 C320,290 190,182 0,178 Z" fill="var(--green-dark)"/>
    <path d="M0,192 C190,198 310,300 444,400 L0,400 Z" fill="url(#front-green)"/>
  </svg>

  <div class="brand">
    <span class="brand__dot"></span>
    <span class="brand__name">GreenLoop</span>
  </div>

  <div class="person">
    <p class="person__name">NORA K. HALE</p>
    <p class="person__role">Executive Director</p>
  </div>

  <ul class="contact">
    <li class="contact__item">555-204-3817
      <svg class="contact__icon" viewBox="0 0 18 18"><circle cx="9" cy="9" r="9" fill="var(--green-mid)"/><rect x="6" y="4" width="6" height="10" rx="1.2" fill="#fff"/></svg></li>
    <li class="contact__item">555-204-3902
      <svg class="contact__icon" viewBox="0 0 18 18"><circle cx="9" cy="9" r="9" fill="var(--green-mid)"/><rect x="5" y="7" width="8" height="6" rx="1" fill="#fff"/><rect x="6.5" y="4" width="5" height="3" fill="#fff"/></svg></li>
    <li class="contact__item">555-204-3955
      <svg class="contact__icon" viewBox="0 0 18 18"><circle cx="9" cy="9" r="9" fill="var(--green-mid)"/><path d="M6,4 L8,4 L9,7 L7.6,8 C8.3,9.6 9.4,10.7 11,11.4 L12,10 L15,11 L15,13 C10,13.5 5,9 5,5 Z" fill="#fff"/></svg></li>
    <li class="contact__item">hello@greenloopmail.com
      <svg class="contact__icon" viewBox="0 0 18 18"><circle cx="9" cy="9" r="9" fill="var(--green-mid)"/><rect x="4.5" y="5.5" width="9" height="7" rx="1" fill="#fff"/><path d="M4.5,6 L9,9.5 L13.5,6" stroke="var(--green-mid)" stroke-width="1" fill="none"/></svg></li>
    <li class="contact__item">www.greenloopdepot.com
      <svg class="contact__icon" viewBox="0 0 18 18"><circle cx="9" cy="9" r="9" fill="var(--green-mid)"/><circle cx="9" cy="9" r="4.5" stroke="#fff" stroke-width="1.3" fill="none"/><path d="M4.5,9 H13.5 M9,4.5 V13.5" stroke="#fff" stroke-width="1"/></svg></li>
  </ul>

  <p class="address">PO Box 48, Fernhill Road<br>Ashby Park, USA</p>
</section>

<section class="card card--back" aria-label="Business card back">
  <svg class="card__art" viewBox="0 0 700 400" aria-hidden="true">
    <defs>
      <linearGradient id="back-green" x1="0" y1="0" x2="1" y2="1">
        <stop offset="0" stop-color="#5ab946"/>
        <stop offset="1" stop-color="#9ccc3a"/>
      </linearGradient>
    </defs>
    <path d="M0,0 L700,0 L700,196 C560,108 380,40 0,26 Z" fill="url(#back-green)"/>
    <path d="M260,46 C460,80 600,150 700,212 L700,232 C580,160 440,92 260,46 Z" fill="var(--green-dark)"/>
    <path d="M0,266 C230,270 450,330 560,400 L525,400 C420,345 230,296 0,292 Z" fill="var(--green-dark)"/>
    <path d="M0,304 C200,308 380,350 480,400 L0,400 Z" fill="url(#back-green)"/>
  </svg>

  <div class="brand">
    <span class="brand__dot"></span>
    <span class="brand__name">GreenLoop</span>
  </div>
</section>

</body>
</html>
```